Verdalo sage- referral cards for new customers

Hey,

I would like 1 set of business cards with the following details:

10% off any sales / coupon code
Our phone number: 5302749186
Menu :Verdalosage.example (for the menu)
A line left blank to hand write an activation code: either on top or just on one side

Include the Verdalo Sage logo ( your choice of black or white logo)
This card is to drive orders for people to order a cannabis order with Verdalo Sage. Please make the logo a large part of the card on both sides.

Target Market(s)

People who consume cannabis 21 and up

Industry/Entity Type

Business

Contact Information for Business Card

This business card will be given to customers so they can then give it to other customers and generate referalls. We need this card to be elegant, impressionable, professional, and something worth keeping and passing to friends.

Font styles to use
Decorative
Script

Colors
33a6d7
85acd3
3176b5
0455a3
0592cd
85cae6
cee9f5
eaf1f7
757575

Requirements
Must have
• Our website
• Phone Number
• The 10% off an order
• Spot for activation code
Nice to have
• Eye catching design
• Look classy
• Textured feel or textured look
Should not have
• Do not look super cannabis heady
• Do not look attractive to children

```html
<!DOCTYPE html>
<html lang="en">
<head>
<meta charset="utf-8">
<title>Verdalo Sage – Referral Cards</title>
<link href="https://fonts.googleapis.com/css2?family=Anton&family=Arvo:wght@700&family=Kaushan+Script&family=Roboto:wght@400&family=Yellowtail&display=block" rel="stylesheet">
<style>
  :root {
    --backdrop: #e9e6e1;
    --card-red: #d14327;
    --card-paper: #f0f0f0;
    --ink: #111111;
    --ink-soft: #555555;
    --white: #ffffff;
    --gold: #e8b923;
    --art-olive: #5b6426;
    --art-teal: #b9e1e5;
    --art-dark: #2e2a33;
  }
  * { box-sizing: border-box; margin: 0; padding: 0; }
  html, body { width: 1200px; height: 960px; overflow: hidden; }
  body { background: var(--backdrop); position: relative; font-family: "Roboto", sans-serif; }

  .card {
    position: absolute;
    width: 600px;
    height: 343px;
    overflow: hidden;
    box-shadow: 2px 3px 6px rgba(0,0,0,0.25);
  }
  .card--coupon { left: 314px; top: 113px; background: var(--card-red); }
  .card--brand { left: 311px; top: 472px; background: var(--card-red); }

  .coupon-paper { position: absolute; inset: 0; }

  .coupon-label {
    position: absolute; left: 36px; top: 50px;
    font-family: "Arvo", serif; font-weight: 700; font-size: 13px;
    color: var(--ink-soft);
  }
  .write-line {
    position: absolute; left: 35px; width: 155px;
    border-top: 1.5px dotted #777;
  }
  .write-line--1 { top: 91px; }
  .write-line--2 { top: 109px; }

  .contact {
    position: absolute; left: 38px; top: 207px;
    font-family: "Arvo", serif; font-weight: 700; font-size: 13.5px;
    line-height: 20px; letter-spacing: 0.4px; color: var(--white);
    white-space: nowrap;
  }

  .offer { position: absolute; left: 35px; top: 262px; height: 70px; width: 200px; }
  .offer-percent {
    position: absolute; left: 0; top: 0;
    font-family: "Anton", sans-serif; font-size: 58px; line-height: 66px;
    color: var(--gold); letter-spacing: -1px;
  }
  .offer-off {
    position: absolute; left: 110px; top: -6px;
    font-family: "Anton", sans-serif; font-size: 50px; line-height: 60px;
    color: var(--white);
  }
  .offer-note {
    position: absolute; left: 111px; top: 36px;
    font-family: "Yellowtail", "Kaushan Script", cursive; font-size: 19px; line-height: 24px;
    color: var(--ink); white-space: nowrap; transform: rotate(-4deg);
    text-shadow: 1px 1px 0 var(--white), -1px -1px 0 var(--white), 1px -1px 0 var(--white), -1px 1px 0 var(--white);
  }

  .brand-art {
    position: absolute; border-radius: 50%;
    background: radial-gradient(circle at 50% 45%, var(--art-teal) 0 22%, var(--art-dark) 34%, var(--art-olive) 56%, rgba(91,100,38,0) 72%);
  }
  .card--coupon .brand-art { left: 342px; top: 12px; width: 234px; height: 206px; }
  .card--brand .brand-art { left: 4px; top: 6px; width: 376px; height: 332px; }

  .brand-name {
    position: absolute; font-family: "Roboto", sans-serif; font-weight: 400;
    color: var(--ink); white-space: nowrap; letter-spacing: 1px;
  }
  .card--coupon .brand-name { left: 361px; top: 222px; font-size: 30px; }
  .card--brand .brand-name { left: 360px; top: 243px; font-size: 30px; }

  .brand-url {
    position: absolute; left: 361px; top: 295px;
    font-family: "Roboto", sans-serif; font-size: 13px; color: var(--white);
    white-space: nowrap;
  }
</style>
</head>
<body>

  <section class="card card--coupon" aria-label="Coupon side">
    <svg class="coupon-paper" width="600" height="343" viewBox="0 0 600 343" aria-hidden="true">
      <polygon points="0,0 600,0 600,270 346,270 271,178 0,178" fill="var(--card-paper)"/>
    </svg>

    <p class="coupon-label">Coupon code: .</p>
    <div class="write-line write-line--1"></div>
    <div class="write-line write-line--2"></div>

    <p class="contact">
      PHONE : 5302749186<br>
      MENU : VERDALOSAGE.EXAMPLE
    </p>

    <div class="offer">
      <span class="offer-percent">10%</span>
      <span class="offer-off">OFF</span>
      <span class="offer-note">any sales</span>
    </div>

    <div class="brand-art" role="img" aria-label="Brand illustration emblem with leaves and a round patterned frame"></div>
    <p class="brand-name">Verdalo Sage</p>
  </section>

  <section class="card card--brand" aria-label="Brand side">
    <div class="brand-art" role="img" aria-label="Large brand illustration emblem with leaves and a round patterned frame"></div>
    <p class="brand-name">Verdalo Sage</p>
    <p class="brand-url">WWW.VERDALOSAGE.EXAMPLE</p>
  </section>

</body>
</html>
```